Floristry Business Card Design Project

I have a logo now and am looking to incorporate this into a business card. I would like a double sided business card. I would like one side to be decorative so that it blends well when included with floral arrangements and that can also be used as the front of a card and the other side will contain the business details. The font on the business details side should be clear although some decorative font would be ok. I have included the logo files for use in the business card design.

Feel free to break up the logo and use certain aspects of it in the design. Really looking for something that stands out and that is really creative.

Industry/Entity Type

Floral

Requirements
Should not have
• Nothing tacky or corny. The logo should be clearly read (perhaps a background colour).

```html
<!DOCTYPE html>
<html lang="en">
<head>
<meta charset="utf-8">
<title>Petal Hollow – Business Card</title>
<link rel="stylesheet" href="https://fonts.googleapis.com/css2?family=Cinzel:wght@400&family=Cormorant+Garamond:wght@400&display=swap">
<style>
  :root {
    --page-bg: #2e2e2e;
    --card-white: #f4f5f3;
    --band-dark: #2a2a2a;
    --band-edge: #3a3a3a;
    --title-green: #a8c990;
    --contact-green: #86b99a;
    --lime: #b6c77f;
    --sage: #80b79b;
    --badge-white: #f7f8f5;
    --badge-text: #6fa585;
    --halo: rgba(255, 255, 255, 0.14);
  }
  html, body {
    margin: 0;
    width: 1200px;
    height: 900px;
    overflow: hidden;
    background: var(--page-bg);
  }
  .canvas {
    width: 1200px;
    height: 900px;
    display: flex;
    flex-direction: column;
    align-items: center;
    justify-content: center;
    gap: 40px;
  }
  .card {
    position: relative;
    width: 700px;
    height: 400px;
    border-radius: 10px;
    overflow: hidden;
    box-shadow: 0 10px 30px rgba(0, 0, 0, 0.45);
  }

  /* Details side */
  .card--details { background: var(--card-white); }
  .title-band {
    position: absolute;
    left: 0; top: 0;
    width: 100%;
    height: 78px;
    background: linear-gradient(180deg, var(--band-edge), var(--band-dark));
  }
  .title-band__tab {
    position: absolute;
    right: 60px;
    top: 78px;
    width: 36px;
    height: 18px;
  }
  .title-band__name {
    position: absolute;
    left: 48px;
    top: 0;
    height: 78px;
    display: flex;
    align-items: center;
    margin: 0;
    font-family: "Cinzel", serif;
    font-weight: 400;
    font-size: 38px;
    letter-spacing: 0.32em;
    color: var(--title-green);
  }
  .contact {
    position: absolute;
    right: 56px;
    top: 118px;
    margin: 0;
    text-align: right;
    font-family: "Cormorant Garamond", serif;
    font-size: 27px;
    line-height: 1.6;
    color: var(--contact-green);
    font-style: normal;
  }
  .contact__line { display: block; }
  .contact__line--person { font-size: 25px; }
  .details-mark {
    position: absolute;
    left: 90px;
    bottom: 48px;
    display: flex;
    align-items: center;
    gap: 14px;
    font-family: "Cinzel", serif;
    font-size: 22px;
    letter-spacing: 0.08em;
    color: var(--badge-text);
  }
  .details-mark__dot {
    width: 26px; height: 26px;
    border-radius: 50%;
    background: var(--contact-green);
  }

  /* Decorative side */
  .card--cover {
    background: linear-gradient(180deg, var(--lime) 0 41%, var(--sage) 41% 100%);
  }
  .cover-halo {
    position: absolute;
    left: 50%; top: 50%;
    width: 300px; height: 300px;
    margin: -150px 0 0 -150px;
    border-radius: 50%;
    background: var(--halo);
  }
  .cover-badge {
    position: absolute;
    left: 50%; top: 50%;
    width: 220px; height: 220px;
    margin: -110px 0 0 -110px;
    border-radius: 50%;
    background: var(--badge-white);
    display: flex;
    align-items: center;
    justify-content: center;
    text-align: center;
    font-family: "Cinzel", serif;
    font-size: 26px;
    line-height: 1.3;
    letter-spacing: 0.08em;
    color: var(--badge-text);
  }
</style>
</head>
<body>
<main class="canvas">
  <section class="card card--details" aria-label="Business details side">
    <div class="title-band">
      <h1 class="title-band__name">Petal Hollow</h1>
    </div>
    <svg class="title-band__tab" viewBox="0 0 36 18" aria-hidden="true">
      <polygon points="0,0 36,0 18,18" fill="var(--band-dark)"/>
    </svg>
    <address class="contact">
      <span class="contact__line contact__line--person">Alex Morgan</span>
      <span class="contact__line">alex@petalhollow.com</span>
      <span class="contact__line">5550-123-47</span>
      <span class="contact__line">petalhollow.com</span>
    </address>
    <div class="details-mark">
      <span class="details-mark__dot"></span>
      <span>Petal Hollow</span>
    </div>
  </section>

  <section class="card card--cover" aria-label="Decorative cover side">
    <div class="cover-halo"></div>
    <div class="cover-badge">Petal<br>Hollow</div>
  </section>
</main>
</body>
</html>
```